Business Cards

Business cards (double-sided) to be handed out to clients and potential clients, with contact details, logo .

Target Market(s)

Small to medium size businesses

Industry/Entity Type

Accountants

Contact Information for Business Card

Brightwater Ledger & Counsel Ltd

Colors

Designer to choose only greyscale colors for use in the design.

Requirements
Must have
• Name, Title, Address, Phone number, Email, Website
Nice to have
• Modern, clean lines, classy
Should not have
• Business cards to be double-sided. Form keeps reverting to single-sided.

```html
<!DOCTYPE html>
<html lang="en">
<head>
<meta charset="utf-8">
<title>Brightwater Ledger &amp; Counsel – Business Card</title>
<link href="https://fonts.googleapis.com/css2?family=Josefin+Sans:wght@300&family=Roboto:wght@400;700&display=swap" rel="stylesheet">
<style>
  :root {
    --backdrop: #3a3a3c;
    --card-silver: #b4b4b6;
    --card-black: #1c1c1e;
    --ink-dark: #111112;
    --ink-light: #f2f2f2;
    --ink-muted: #d9d9d9;
  }
  * { margin: 0; padding: 0; box-sizing: border-box; }
  html, body {
    width: 1200px;
    height: 1000px;
    overflow: hidden;
    background: var(--backdrop);
  }
  .canvas {
    position: relative;
    width: 1200px;
    height: 1000px;
  }
  .card {
    position: absolute;
    left: 250px;
    width: 700px;
    height: 400px;
    border-radius: 22px;
  }
  .card--front {
    top: 70px;
    background: linear-gradient(160deg, #c0c0c2 0%, var(--card-silver) 60%, #a9a9ab 100%);
    display: flex;
    align-items: center;
    justify-content: center;
  }
  .card--back {
    top: 530px;
    background: linear-gradient(160deg, #2a2a2c 0%, var(--card-black) 55%, #141415 100%);
  }
  .brand-name {
    font-family: "Josefin Sans", sans-serif;
    font-weight: 300;
    letter-spacing: 0.14em;
    text-transform: uppercase;
    line-height: 1.25;
  }
  .card--front .brand-name {
    color: var(--ink-dark);
    font-size: 40px;
    text-align: left;
  }
  .card--back .brand-name {
    position: absolute;
    left: 60px;
    top: 110px;
    color: var(--ink-muted);
    font-size: 24px;
  }
  .contact {
    position: absolute;
    right: 60px;
    top: 150px;
    text-align: right;
    font-family: "Roboto", sans-serif;
    color: var(--ink-light);
  }
  .contact__name {
    font-weight: 700;
    font-size: 24px;
    letter-spacing: 0.02em;
  }
  .contact__title {
    font-weight: 400;
    font-size: 21px;
    margin-top: 4px;
  }
  .contact__details {
    list-style: none;
    margin-top: 34px;
    font-size: 19px;
    line-height: 1.2;
  }
</style>
</head>
<body>
  <main class="canvas">
    <section class="card card--front" aria-label="Business card front">
      <p class="brand-name">Brightwater<br>Ledger &amp; Counsel</p>
    </section>

    <section class="card card--back" aria-label="Business card back">
      <p class="brand-name">Brightwater<br>Ledger &amp; Counsel</p>
      <div class="contact">
        <p class="contact__name">Elena Marsh</p>
        <p class="contact__title">Title</p>
        <ul class="contact__details">
          <li>Address,</li>
          <li>Phone number,</li>
          <li>Email,</li>
          <li>Website</li>
        </ul>
      </div>
    </section>
  </main>
</body>
</html>
```